We need a new menu with more professional outlook for our restaurant called Mei Tan Garden Vegetarian Cuisine. We are vegetarian restaurant offered healthy food with nice environment and service. Our restaurant's pictures and take away menu are available on www.meitan-eatery.com.au. I want to redesign our eat in and take away menu to be similar to our restaurant's theme and something which is green, healthy and professional. I gave the menu of my favorite restaurant on Google Docs.
Updates
Dear all,
Industry/Entity Type
Environment
Requirements
Must have
- I am really interested in the design and layout of the restaurant in our local area- please refer to these files: https://files.example-share.net/open?id=7Q-KpzeWTrmLhQaTnfXo4PvNkRsE and https://files.example-share.net/open?id=7Q-KpzeWTrmLhBvR9WcXa2LqMhT . We would like something look like this: simple, easy to follow and professional.

```html
<!DOCTYPE html>
<html lang="en">
<head>
<meta charset="utf-8">
<title>Mei Tan Garden Vegetarian Cuisine — Menu</title>
<link href="https://fonts.googleapis.com/css2?family=PT+Sans:wght@400;700&family=Tinos:wght@400&display=swap" rel="stylesheet">
<style>
  :root{
    --band-orange:#E9A024;
    --strip-green:#8DC63F;
    --head-orange:#F2A12B;
    --head-green:#6DB33F;
    --price-orange:#F39A1E;
    --ink:#1d1d1d;
    --paper:#ffffff;
  }
  *{margin:0;padding:0;box-sizing:border-box}
  html,body{width:1200px;height:900px;overflow:hidden;background:var(--paper)}
  .menu{position:relative;width:1200px;height:900px;overflow:hidden;background:var(--paper);font-family:"Tinos","Times New Roman",serif;color:var(--ink)}
  .band-top{position:absolute;left:0;top:0;width:1200px;height:20px;background:var(--band-orange)}
  .band-bottom{position:absolute;left:0;top:815px;width:1200px;height:85px;background:var(--band-orange)}
  .side-pattern{position:absolute;top:20px;width:70px;height:795px;background:linear-gradient(180deg,#93C944,#85BF39)}
  .side-pattern.left{left:0}
  .side-pattern.right{right:0}
  .column{position:absolute;top:62px}
  .col-1{left:85px;width:278px}
  .col-2{left:417px;width:323px;top:60px}
  .col-3{left:790px;width:320px;top:60px}
  .section-title{font-family:"PT Sans",sans-serif;font-weight:700;font-size:21px;text-align:center;line-height:24px;height:24px;color:var(--head-orange);letter-spacing:.2px;margin-bottom:4px}
  .section-title .green{color:var(--head-green)}
  .section-title.noodle{color:var(--head-green);font-size:17px;line-height:20px;height:20px;margin-bottom:0}
  .section-sub{font-family:"PT Sans",sans-serif;font-weight:700;font-size:11px;line-height:14px;color:var(--head-green);text-align:center;margin-bottom:22px}
  .item{display:flex;align-items:baseline;font-size:10px;line-height:16.6px;height:16.6px;text-transform:uppercase;white-space:nowrap;overflow:hidden}
  .item .dots{flex:1;border-bottom:1px dotted #555;margin:0 1px 3px;min-width:6px}
  .item .price{font-family:"PT Sans",sans-serif;font-weight:700;font-size:12.5px;line-height:1;color:var(--price-orange)}
  .item .note{text-transform:none}
  .item.indent{padding-left:5px;text-transform:none}
  .item.indent .cap{text-transform:uppercase}
  .item small{font-size:8px}
  .col-2 > .item{height:19.5px;line-height:19.5px}
  .entry{margin-bottom:8.5px}
  .entry .item{height:15px;line-height:15px}
  .desc{font-size:9.5px;line-height:11.5px}
  .gap-s{height:24px}
  .gap-c2{height:28px}
  .gap-m{height:10px}
  .footer-title{position:absolute;left:0;width:1200px;top:834px;text-align:center;font-family:"PT Sans",sans-serif;font-weight:700;font-size:28px;line-height:40px;color:#111;letter-spacing:.3px}
  .go-green{position:absolute;top:843px;display:flex;align-items:center;gap:8px;font-family:"PT Sans",sans-serif;font-size:21px;line-height:28px;color:#fff}
  .go-green.left{left:52px}
  .go-green.right{left:935px}
</style>
</head>
<body>
<main class="menu">
  <div class="band-top"></div>
  <div class="side-pattern left" role="img" aria-label="Green strip with repeating fleur-de-lis pattern"></div>
  <div class="side-pattern right" role="img" aria-label="Green strip with repeating fleur-de-lis pattern"></div>

  <section class="column col-1">
    <h2 class="section-title">APPETIZERS</h2>
    <div class="item"><span>Mei Tan Special Spring Rolls (4 Rolls)</span><span class="dots"></span><span class="price">$6.90</span></div>
    <div class="item"><span>Vegetarian Spring Rolls (4 Rolls)</span><span class="dots"></span><span class="price">$6.90</span></div>
    <div class="item"><span>Shredded Tofu Rolls (2 Rolls)</span><span class="dots"></span><span class="price">$5.50</span></div>
    <div class="item"><span>Fresh Cold Rolls (2 Rolls)</span><span class="dots"></span><span class="price">$5.50</span></div>
    <div class="item"><span>Pocket Money Bags (6 Pieces)</span><span class="dots"></span><span class="price">$6.90</span></div>
    <div class="item"><span>Deep-Fried Wonton (5 Pieces)</span><span class="dots"></span><span class="price">$6.90</span></div>
    <div class="item"><span>Deep-Fried Tofu (5 Pieces)</span><span class="dots"></span><span class="price">$6.90</span></div>
    <div class="item"><span>Soy Chicken Nuggets (7 Pieces)</span><span class="dots"></span><span class="price">$6.90</span></div>
    <div class="item"><span>Soy Chicken Drumsticks (5 Pieces)</span><span class="dots"></span><span class="price">$6.90</span></div>
    <div class="item"><span>Soy Chicken Satay Skewers (6 Skewers)</span><span class="dots"></span><span class="price">$6.90</span></div>
    <div class="item"><span>Mushroom Fritters (5Pieces)</span><span class="dots"></span><span class="price">$6.90</span></div>
    <div class="item"><span>Eggplant Fritters (5 Pieces)</span><span class="dots"></span><span class="price">$6.90</span></div>
    <div class="item"><span>Soy Crabmeat Pate <span class="note">(Served with crackers)</span></span><span class="dots"></span><span class="price">$7.90</span></div>
    <div class="item"><span>B.B.Q Soy Meat Skewers (2 Skewers)</span><span class="dots"></span><span class="price">$8.00</span></div>
    <div class="item"><span>Curry Puff (4 Pieces)</span><span class="dots"></span><span class="price">$7.00</span></div>
    <div class="item"><span>Soy Shrimp on Toast (4 Pieces</span><span class="dots"></span><span class="price">$6.90</span></div>
    <div class="item"><span>Soy Chicken Salad</span><span class="dots"></span><span class="price">$11.00</span></div>
    <div class="item"><span>Mei Tan Special Salad <span class="note">(Served with crackers)</span></span><span class="dots"></span><span class="price">$11.00</span></div>
    <div class="item"><span>Paw Paw Salad <span class="note">(Served with crackers)</span></span><span class="dots"></span><span class="price">$11.00</span></div>
    <div class="item"><span>Asparagus Soup</span><span class="dots"></span><span class="price">$7.90</span></div>
    <div class="item"><span>Corn Soup</span><span class="dots"></span><span class="price">$7.90</span></div>
    <div class="item"><span>Wonton Soup</span><span class="dots"></span><span class="price">$7.90</span></div>
    <div class="item"><span>Soy Duck Wraps (4 Wraps)</span><span class="dots"></span><span class="price">$7.90</span></div>
    <div class="item"><span>Veggies Dumpling (5 Pieces)</span><span class="dots"></span><span class="price">$6.90</span></div>
    <div class="item"><span>Vegetable Steamed Buns (4 Buns)</span><span class="dots"></span><span class="price">$6.90</span></div>
    <div class="gap-s"></div>
    <h2 class="section-title noodle">VIETNAMESE NOODLE SPECIALTIES</h2>
    <p class="section-sub">(SERVED WITH OR WITHOUT ONION OR SHALLOT)</p>
    <div class="item"><span>Mei Tan Soy Beef Soup</span><span class="dots"></span><span class="price">$12.50</span></div>
    <div class="item"><span>Mei Tan Soy Chicken Soup</span><span class="dots"></span><span class="price">$12.50</span></div>
    <div class="item"><span>Soy Pork Rice Noodle Soup</span><span class="dots"></span><span class="price">$12.50</span></div>
    <div class="item"><span>Soy Pork Dry Rice Noodle Soup</span></div>
    <div class="item indent"><span>(Served with spearate bowl of soup and savory sauce)</span><span class="dots"></span><span class="price">$12.50</span></div>
    <div class="item"><span>Soy Seafood Rice Noodle Soup</span><span class="dots"></span><span class="price">$13.50</span></div>
    <div class="item"><span>Soy Chicken Yellow Noodle Soup</span></div>
    <div class="item"><span>Soy Duck Yellow Noodle Soup</span><span class="dots"></span><span class="price">$12.50</span></div>
    <div class="item"><span>Wonton Yellow Noodle Soup</span><span class="dots"></span><span class="price">$12.50</span></div>
    <div class="item"><span>Combination Laksa Noodle</span><span class="dots"></span><span class="price">$13.50</span></div>
    <div class="item"><span>Royal Noodle Soup (Spicy)</span><span class="dots"></span><span class="price">$12.50</span></div>
    <div class="item"><span>Fresh Starch Home-Made</span></div>
    <div class="item indent"><span class="cap">Noodle Soup</span><span class="dots"></span><span class="price">$12.50</span></div>
  </section>

  <section class="column col-2">
    <div class="item"><span>Rice Vermicelli with Spring Rolls</span><span class="dots"></span><span class="price">$12.50</span></div>
    <div class="item"><span>Rice Vermicelli Spring Rolls &amp; Tofu</span><span class="dots"></span><span class="price">$12.50</span></div>
    <div class="item"><span>Rice Vermicelli with B.B.Q Soy Meat</span><span class="dots"></span><span class="price">$12.50</span></div>
    <div class="item"><span>Combo Soy Meat Veggie Stir Fry Rice Noodle</span><span class="dots"></span><span class="price">$17.00</span></div>
    <div class="item"><span>Combo Soy Seafood Veggie Stir Fry Rice Noodle</span><span class="dots"></span><span class="price">$18.00</span></div>
    <div class="item"><span>Combo Soy Meat Veggie Soft <small>or</small> Crispy Noodle</span><span class="dots"></span><span class="price">$17.00</span></div>
    <div class="item"><span>Combo Soy Seafood Veggie Soft <small>or</small> Crispy Noodle</span><span class="dots"></span><span class="price">$18.00</span></div>
    <div class="gap-c2"></div>
    <h2 class="section-title">FRESH <span class="green">VEGETABLES</span></h2>
    <div class="entry"><div class="item"><span>Budda's Feast</span><span class="dots"></span><span class="price">$14.90</span></div><p class="desc">(Vegetables tossed in clear veggie soup with an exclusive sauce)</p></div>
    <div class="entry"><div class="item"><span>Assorted Steamed Vegetables</span><span class="dots"></span><span class="price">$14.50</span></div><p class="desc">(Freshly prepared vegetables steamed and served with special sauce)</p></div>
    <div class="entry"><div class="item"><span>Curry Vegetable with Coconut Cream</span><span class="dots"></span><span class="price">$14.90</span></div><p class="desc">(Coconut cream sauce with cauliflowers, carrots, broccoli &amp; celery)</p></div>
    <div class="entry"><div class="item"><span>Braised Snow Peas and Abalone Mushroom</span><span class="dots"></span><span class="price">$15.90</span></div><p class="desc">(Fresh vegetables, snow peas and mushroom tossed in a light sauce)</p></div>
    <div class="entry"><div class="item"><span>Braised Green Bean and Soy Beef</span><span class="dots"></span><span class="price">$15.90</span></div><p class="desc">(A mixture of fresh vegetables and green bean tossed in a light sauce)</p></div>
    <div class="entry"><div class="item"><span>Braised Green Bean and Soy Chicken</span><span class="dots"></span><span class="price">$15.90</span></div><p class="desc">(Vegetables tossed in clear veggie soup with an exclusive sauce)</p></div>
    <h2 class="section-title">TOFU <span class="green">DELIGHT</span></h2>
    <div class="entry"><div class="item"><span>Braised Tofu and Vegetable</span><span class="dots"></span><span class="price">$14.90</span></div><p class="desc">(Vegetables tossed in clear veggie soup with an exclusive sauce)</p></div>
    <div class="entry"><div class="item"><span>Stuffed Beancurd in Delight</span></div><div class="item"><span>Sweet &amp; Sour Sauce</span><span class="dots"></span><span class="price">$14.90</span></div><p class="desc">(Tomato &amp; lemon sauce with pinapple, onions, carrots &amp; cucumbers)</p></div>
    <div class="entry"><div class="item"><span>Tofu with Lemon Grass (Spicy)</span><span class="dots"></span><span class="price">$14.90</span></div><p class="desc">(Onions and capsicums, spiced with minced lemongrass &amp; chili)</p></div>
    <div class="entry"><div class="item"><span>Tofu with Satay Sauce (Spicy)</span><span class="dots"></span><span class="price">$14.90</span></div><p class="desc">(Satay sauce with spices, cauliflowers, carrots, broccoli, &amp; celery)</p></div>
    <div class="entry"><div class="item"><span>Braised Tofu &amp; Vegetable with Cashew Nut</span><span class="dots"></span><span class="price">$15.90</span></div><p class="desc">(Vegetables tossed in a light sauce and served with crunchy cashews)</p></div>
    <h2 class="section-title">SOY <span class="green">BEEF</span></h2>
    <div class="entry"><div class="item"><span>Soy Beef Curry &amp; Veggie with Coconut Cream</span><span class="dots"></span><span class="price">$15.90</span></div><p class="desc">(Coconut cream sauce with cauliflowers, carrots, broccoli &amp; celery)</p></div>
    <div class="entry"><div class="item"><span>Soy Beef Stay Sauce (Spicy)</span><span class="dots"></span><span class="price">$15.90</span></div><p class="desc">(Satay sauce with spices, cauliflowers, carrots, broccoli &amp; celery)</p></div>
    <div class="entry"><div class="item"><span>Braised Tofu &amp; Vegetable with Cashew Nut</span><span class="dots"></span><span class="price">$15.90</span></div><p class="desc">(Onions, capsicums and soy beef stirred in a light soy sauce and peanut)</p></div>
  </section>

  <section class="column col-3">
    <div class="entry"><div class="item"><span>Soy Beef and Cashew Nut</span><span class="dots"></span><span class="price">$16.90</span></div><p class="desc">(Vegetables tossed in a light sauce and served with crunchy cashews)</p></div>
    <div class="entry"><div class="item"><span>Soy Beef on Hot Plate</span><span class="dots"></span><span class="price">$15.90</span></div><p class="desc">(Special sauce combined with cauliflowers, carrots, capsicums,<br>celery and onions, served of a hot sizzling plate)</p></div>
    <div class="entry"><div class="item"><span>Soy Beef Ginger</span><span class="dots"></span><span class="price">$15.90</span></div><p class="desc">(Thin ginger strips stir-fried with soy beef with onions, capsicums and salad)</p></div>
    <div class="entry"><div class="item"><span>Soy Beef Rendang</span><span class="dots"></span><span class="price">$15.90</span></div><p class="desc">(Authentic rendang sauce with onions, cucumbers and coriander)</p></div>
    <h2 class="section-title">SOY <span class="green">FISH</span></h2>
    <div class="entry"><div class="item"><span>Fried Soy Fish with Savoury Ginger Sauce</span><span class="dots"></span><span class="price">$15.90</span></div><p class="desc">(Vegetables tossed in a light sauce and served with crunchy cashews)</p></div>
    <div class="entry"><div class="item"><span>Soy Fish in Clay Pot Sensation</span><span class="dots"></span><span class="price">$15.90</span></div><p class="desc">(Onions, capsicums stirred with soy fish drizzled over with<br>exclusive sauce)</p></div>
    <div class="entry"><div class="item"><span>Fried Soy Fish with Lemongrass</span><span class="dots"></span><span class="price">$15.90</span></div><p class="desc">(Onions and capsicums, spiced with minced lemongrass and chili)</p></div>
    <div class="entry"><div class="item"><span>Savory Sweet &amp; Sour Fish</span><span class="dots"></span><span class="price">$15.90</span></div><p class="desc">(Tomato and lemon sauce with pineapple, onions, carrots and cucumbers)</p></div>
    <div class="entry"><div class="item"><span>Soy Fish with Tamarind Sauce</span><span class="dots"></span><span class="price">$15.90</span></div><p class="desc">(Soy fish drizzled over with tamarind sauce and onions)</p></div>
    <div class="entry"><div class="item"><span>Fried Soy Fish with Spicy Salt &amp; Chili</span><span class="dots"></span><span class="price">$16.90</span></div><p class="desc">(Soy fish fillet slightly dressed with salts, chili and served with<br>onions and capsicums)</p></div>
    <div class="gap-m"></div>
    <h2 class="section-title">SOY <span class="green">CHICKEN</span></h2>
    <div class="entry"><div class="item"><span>Honey Roast Soy Chicken</span><span class="dots"></span><span class="price">$15.90</span></div><p class="desc">(Lightly battered soy chicken drizzled in special syrup sauce<br>or honey bee sauce)</p></div>
    <div class="entry"><div class="item"><span>Soy Chicken and Cashew Nut</span><span class="dots"></span><span class="price">$15.90</span></div><p class="desc">(Fresh vegetables tossed in a light sauce and served with crunchy cashews)</p></div>
    <div class="entry"><div class="item"><span>Lemon Grass Soy Chicken (Spicy)</span><span class="dots"></span><span class="price">$15.90</span></div><p class="desc">(Minced lemongrass and chilli carmelized with soy chicken drizzled over<br>with exclusive sauce and served with onions and capsicums)</p></div>
    <div class="entry"><div class="item"><span>Ginger Soy Chicken</span><span class="dots"></span><span class="price">$15.90</span></div><p class="desc">(Thin ginger strips stir-fried with soy chicken &amp; onions, capsicums)</p></div>
    <div class="entry"><div class="item"><span>Soy Chicken Curry &amp; Veggie</span></div><div class="item"><span>with Coconuy Cream</span><span class="dots"></span><span class="price">$15.90</span></div><p class="desc">(Coconut cream sauce with cauliflowers, carrots, brocolli &amp; celery)</p></div>
    <div class="entry"><div class="item"><span>Soy Chicken with Basil Leaf</span><span class="dots"></span><span class="price">$15.90</span></div><p class="desc">(A combination of capsicums and onions with exclusive sauce served salad)</p></div>
    <div class="entry"><div class="item"><span>Soy Chicken Satay Sauce (Spicy)</span><span class="dots"></span><span class="price">$15.90</span></div><p class="desc">(Satay sauce with spices, cauliflower, carrots, broccoli and celery)</p></div>
  </section>

  <div class="band-bottom"></div>
  <div class="go-green left">
    <svg width="44" height="16" role="img" aria-label="Leaf swoosh"><ellipse cx="22" cy="8" rx="20" ry="5" fill="#7DBB3A"/></svg>
    <span>Go Green</span>
    <svg width="44" height="16" role="img" aria-label="Leaf swoosh"><ellipse cx="22" cy="8" rx="20" ry="5" fill="#7DBB3A"/></svg>
  </div>
  <h1 class="footer-title">AUTHENTIC VIETNAMESE VEGETARIAN CUISINE</h1>
  <div class="go-green right">
    <svg width="44" height="16" role="img" aria-label="Leaf swoosh"><ellipse cx="22" cy="8" rx="20" ry="5" fill="#7DBB3A"/></svg>
    <span>Go Green</span>
    <svg width="44" height="16" role="img" aria-label="Leaf swoosh"><ellipse cx="22" cy="8" rx="20" ry="5" fill="#7DBB3A"/></svg>
  </div>
</main>
</body>
</html>
```